Redesign of a growing event production company in atlanta!

www.vorquinstage.com - it's Wix.com site and I'd like to keep it within WIX if possible.
We purchased a new logo and we are looking for a redesign.
We specialize in many different aspects of the event production industry and we want our page to be better segmented, with separation between the audio video lighting and wedding services offered.
We also want this cleaned up, showcasing client feedback and highlighted photos. Our industry is very visual and we want some of our work showcased as well as area for event videos.
We want the ability to add new photos and videos as well as links to our blog. If we can incorporate our blog into the site, that would be great as well.
Attached is the new logo, we are going to have it animated and placed on the site as well. We love the color spectrum of light and the significance to event production. We would like the page to incorporate that.
Updates

There are just a few days left, please submit your final versions, with requested revisions.

Target Market(s)

Women are the main purchasees of our services. brides between 20 - 40, and then corporate event planners...we have a high end market. We are marketing to the people who plan galas and society socials.

Industry/Entity Type

It Company

Number of Pages Required

5+ page

Font styles to use
Sans Serif
Script

Requirements
Must have
• incorporate the same content I currently have on my site.
• A clear but fluid separation between our event production services (Audio Visual) and the wedding services we offer. We MUST also be able to clearly show what we do. We are a one stop show and we want to convey that.
Nice to have
• Color palette based off logo attached

```html
<!DOCTYPE html>
<html lang="en">
<head>
<meta charset="utf-8">
<title>Vorquin Stage</title>
<link href="https://fonts.googleapis.com/css2?family=Open+Sans:wght@400;600;700;800&family=Cinzel:wght@400;700&family=Cormorant+Garamond:wght@400&family=Great+Vibes&display=swap" rel="stylesheet">
<style>
:root{
  --bg:#1a1a1a;
  --panel:#141414;
  --bar:#0e0e0e;
  --text:#ffffff;
  --muted:#8a8a8a;
  --orange:#e8731c;
  --line:#2c2c2c;
  --action:rgba(20,120,190,.85);
}
*{margin:0;padding:0;box-sizing:border-box}
html,body{width:779px;height:1200px;overflow:hidden}
body{background:var(--bg);font-family:"Open Sans",sans-serif;color:var(--text);position:relative}
.abs{position:absolute}

.topbar{left:0;top:0;width:779px;height:68px;background:var(--bar);z-index:3}
.topnav a{position:absolute;top:27px;font-size:9px;color:#fff;text-decoration:none;letter-spacing:.2px;white-space:nowrap}
.brand-cap{left:309px;top:40px;width:160px;height:56px;background:var(--bar);border-radius:0 0 80px 80px;z-index:2}
.brand{left:309px;top:12px;width:160px;text-align:center;z-index:4}
.brand-dot{width:36px;height:36px;border-radius:50%;border:2px solid #777;margin:0 auto;background:#222}
.brand-name{font-size:11px;letter-spacing:1px;margin-top:4px;color:#ddd;font-weight:600}
.brand-sub{font-size:3.5px;letter-spacing:1px;color:#777}

.hero{left:0;top:68px;width:779px;height:400px;background:radial-gradient(ellipse at 50% 30%,#6a5a45 0%,#3a3126 45%,#171310 100%)}
.hero-title{left:0;top:225px;width:779px;text-align:center;font-size:68px;font-weight:800;letter-spacing:-1px;line-height:1}
.hero-text{left:140px;top:304px;width:500px;text-align:center;font-size:12px;line-height:18px;color:#eee}
.hero-arrows{left:357px;top:360px}

.panel{background:var(--panel)}
.panel-title{position:absolute;font-size:15px;font-weight:700;letter-spacing:.3px}
.pager{position:absolute}

.gallery{left:51px;top:432px;width:677px;height:284px}
.tile{position:absolute;top:50px;width:157px;height:211px}
.tile-title{position:absolute;left:7px;width:148px;font-family:"Cinzel",serif;font-size:15px;line-height:19px;font-weight:700;color:#fff}
.tile-text{position:absolute;left:7px;top:131px;width:140px;font-size:6.4px;line-height:13px;color:#fff}
.tile-icons{position:absolute;left:7px;top:179px;display:flex;gap:7px}
.tile-icons span{width:15px;height:15px;border:1px solid #fff;border-radius:50%}

.blog{left:51px;top:735px;width:469px;height:343px}
.post{position:absolute;left:13px;width:440px;height:120px}
.post-img{position:absolute;left:0;top:0;width:151px;height:120px;border:1px solid #444}
.post-actions{position:absolute;top:0;width:27px;height:94px;background:var(--action);font-size:7px;text-align:center}
.post-actions div{margin-top:8px}
.post-title{position:absolute;left:170px;top:0;font-size:10px;font-weight:400;color:#eee}
.post-meta{position:absolute;left:170px;top:24px;font-size:7px;color:var(--muted);display:flex;gap:18px}
.post-meta u{color:var(--orange)}
.post-text{position:absolute;left:170px;top:46px;width:265px;font-size:6.4px;line-height:13px;color:var(--muted)}
.btn{position:absolute;left:170px;top:97px;width:70px;height:23px;background:var(--orange);font-size:8px;line-height:23px;text-align:center;color:#fff}
.divider{left:182px;top:184px;width:273px;height:1px;background:var(--line)}

.side{left:534px;top:735px;width:194px;height:343px}
.video{left:10px;top:42px;width:172px;height:122px;background:linear-gradient(#5a4f42,#2a2520);border:1px solid #444}
.video-bar{left:0;bottom:0;width:100%;height:16px;background:#222}
.video-tool{right:4px;width:16px;height:16px;background:rgba(0,0,0,.6);border-radius:2px}
.play{left:70px;top:38px}
.event{position:absolute;left:8px;width:180px;height:60px}
.event-day{position:absolute;left:0;top:0;font-family:"Cormorant Garamond",serif;font-size:26px;line-height:26px;color:#ccc}
.event-mon{position:absolute;left:1px;top:26px;font-family:"Great Vibes",cursive;font-size:18px;line-height:18px;color:#aaa}
.event-title{position:absolute;left:44px;top:2px;font-size:9.5px;font-weight:400;color:#eee}
.event-text{position:absolute;left:44px;top:20px;width:128px;font-size:5.6px;line-height:11px;color:var(--muted)}

.rule{left:0;top:1107px;width:779px;height:2px;background:var(--orange)}
.footer{left:0;top:1109px;width:779px;height:91px;background:var(--bar)}
.footnav{position:absolute;top:20px;left:0;width:779px;text-align:center;font-size:8.2px}
.footnav span{margin:0 9px;color:#fff}
.copy{position:absolute;left:66px;top:62px;font-size:6.5px}
.social{position:absolute;left:584px;top:58px;display:flex;gap:7px}
.social span{width:21px;height:21px;border:1px solid #444;border-radius:50%}
</style>
</head>
<body>

<div class="abs hero" role="img" aria-label="Concert crowd with raised hands under warm stage lights"></div>
<div class="abs hero-title">VORQUIN STAGE</div>
<p class="abs hero-text">It is a long established fact that a reader will be distracted by the readable content of a page when content of a page when looking at its layout.</p>
<svg class="abs hero-arrows" width="66" height="30" viewBox="0 0 66 30">
  <circle cx="15" cy="15" r="13" fill="none" stroke="#fff" stroke-width="1.6"/>
  <path d="M18 8 L11 15 L18 22" fill="none" stroke="#fff" stroke-width="1.8"/>
  <circle cx="50" cy="15" r="13" fill="none" stroke="#fff" stroke-width="1.6"/>
  <path d="M47 8 L54 15 L47 22" fill="none" stroke="#fff" stroke-width="1.8"/>
</svg>

<header class="abs topbar">
  <nav class="topnav">
    <a style="left:74px">HOME</a>
    <a style="left:144px">GET INSPIRED</a>
    <a style="left:246px">SERVICES OFFERED</a>
    <a style="left:446px">VORQUIN OWNERS</a>
    <a style="left:547px">CLIENT REFERRALS</a>
    <a style="left:657px">CONTACT US</a>
  </nav>
</header>
<div class="abs brand-cap"></div>
<div class="abs brand">
  <div class="brand-dot"></div>
  <div class="brand-name">VORQUIN STAGE</div>
  <div class="brand-sub">EVENT PRODUCTION</div>
</div>

<section class="abs panel gallery">
  <h2 class="panel-title" style="left:13px;top:17px">PHOTO GALLERY</h2>
  <svg class="pager" style="right:22px;top:18px" width="24" height="14" viewBox="0 0 24 14">
    <path d="M8 1 L2 7 L8 13 M16 1 L22 7 L16 13" fill="none" stroke="#ddd" stroke-width="2"/>
  </svg>
  <div class="tile" style="left:13px;background:linear-gradient(#d9781c,#b8560f)" role="img" aria-label="Reception hall draped in orange lights">
    <div class="tile-title" style="top:85px">DISC JOCKEYS &amp; EMCEES</div>
    <div class="tile-text">It is a long established fact that a reader will be distracted by the readable content of a page when looking at its layout.</div>
    <div class="tile-icons"><span></span><span></span><span></span><span></span><span></span></div>
  </div>
  <div class="tile" style="left:177px;background:linear-gradient(#4d6a3a,#6b4a2e)" role="img" aria-label="Wedding reception tables under green lighting">
    <div class="tile-title" style="top:166px">WEDDING SOFT TONES</div>
  </div>
  <div class="tile" style="left:341px;background:linear-gradient(#3a2820,#201612)" role="img" aria-label="Prom venue with string lights">
    <div class="tile-title" style="top:166px">PROM AND SOCIAL LIGHTING</div>
  </div>
  <div class="tile" style="left:507px;background:linear-gradient(#8a7d6c,#3e362e)" role="img" aria-label="Ballroom with chandeliers and wedding dance">
    <div class="tile-title" style="top:165px">WEDDING CLUB TONES</div>
  </div>
</section>

<section class="abs panel blog">
  <h2 class="panel-title" style="left:13px;top:17px">LATEST BLOG</h2>
  <svg class="pager" style="right:22px;top:18px" width="20" height="14" viewBox="0 0 20 14">
    <path d="M7 1 L2 7 L7 13 M13 1 L18 7 L13 13" fill="none" stroke="#ddd" stroke-width="2"/>
  </svg>
  <article class="post" style="top:48px">
    <div class="post-img" style="background:linear-gradient(120deg,#2a6ab0,#b03a4a,#d08a30)" role="img" aria-label="Guests dancing at a party"></div>
    <div class="post-actions" style="left:124px"><div>♡<br>Like</div><div>◷<br>Later</div><div>↗<br>Share</div></div>
    <h3 class="post-title">Neque porro quisquam est qui dolorem</h3>
    <div class="post-meta"><span>Date <u>22 Jan 2015</u></span><span>Written by <u>Admin</u></span><span>Comments <u>277</u></span></div>
    <p class="post-text">It is a long established fact that a reader will be distracted by the readable content of a page when looking at its layout. The point of using Lorem Ipsum is that it has a more-or-less normal distribution of letters making it look like readable English</p>
    <div class="btn">LEARN MORE</div>
  </article>
  <div class="abs divider"></div>
  <article class="post" style="top:198px">
    <div class="post-img" style="background:linear-gradient(#c06a20,#2a1a10)" role="img" aria-label="Concert crowd silhouettes against stage lights"></div>
    <div class="post-actions" style="left:124px"><div>♡<br>Like</div><div>◷<br>Later</div><div>↗<br>Share</div></div>
    <h3 class="post-title">Neque porro quisquam est qui dolorem</h3>
    <div class="post-meta"><span>Date <u>22 Jan 2015</u></span><span>Written by <u>Admin</u></span><span>Comments <u>277</u></span></div>
    <p class="post-text">It is a long established fact that a reader will be distracted by the readable content of a page when looking at its layout. The point of using Lorem Ipsum is that it has a more-or-less normal distribution of letters making it look like readable English</p>
    <div class="btn">LEARN MORE</div>
  </article>
</section>

<aside class="abs panel side">
  <h2 class="panel-title" style="left:8px;top:17px">OUR VIDEO</h2>
  <div class="abs video" role="img" aria-label="Video of a wedding dance in a ballroom">
    <div class="abs video-tool" style="top:10px"></div>
    <div class="abs video-tool" style="top:30px"></div>
    <svg class="abs play" width="32" height="32" viewBox="0 0 32 32">
      <circle cx="16" cy="16" r="15" fill="rgba(0,0,0,.55)" stroke="#fff" stroke-width="1.5"/>
      <path d="M13 10 L22 16 L13 22Z" fill="#fff"/>
    </svg>
    <div class="abs video-bar"></div>
  </div>
  <h2 class="panel-title" style="left:8px;top:186px">UPCOMING EVENTS</h2>
  <div class="event" style="top:215px">
    <div class="event-day">25</div><div class="event-mon">jan</div>
    <div class="event-title">Neque porro quisquam</div>
    <div class="event-text">It is a long established fact that a reader of a page when looking at its layout.</div>
  </div>
  <div class="event" style="top:279px">
    <div class="event-day">25</div><div class="event-mon">jan</div>
    <div class="event-title">Neque porro quisquam</div>
    <div class="event-text">It is a long established fact that a reader of a page when looking at its layout.</div>
  </div>
</aside>

<div class="abs rule"></div>
<footer class="abs footer">
  <nav class="footnav"><span>HOME</span>|<span>GET INSPIRED</span>|<span>SERVICES OFFERED</span>|<span>VORQUIN OWNERS</span>|<span>CLIENT REFERRALS</span>|<span>CONTACT US</span></nav>
  <div class="copy">© Copy Rights 2015 Vorquin Stage.All Rights Reserved.</div>
  <div class="social"><span></span><span></span><span></span><span></span><span></span></div>
</footer>

</body>
</html>
```